KEV.PRO- Darren Holcombe Fitness- needs a clever business card using the logo, name, info, contact

I need a business card designed for my Online Personal Training company called KEV.PRO, abbreviation for Darren Holcombe Fitness. My company focuses on coaching in personal health and personal growth to unleash your greatest potential. I would like to see designs that use my color scheme of a redish-orange (C:0,M:84,Y:100,K:0), grey, white, black, and my company font is OSWALD. The final design should communicate some aspects of design, health, motivation, growth, in some way. The logo is very important to the company and can be displayed in any of the colors previously mentioned. Must include the company name, my website: www.kev-pro.example , my email: dan@kev-pro.example

Target Market(s)

Personal health, fitness, general public, those who lack knowledge, awareness, and confidence in personal health

Industry/Entity Type

Personal Trainer

Font styles to use
Other font styles liked:
• OSWALD. (Bold, Regular, Light)

Colors
f37122
ffffff
9d9d9d
000000

Requirements
Must have
• Must include the logo, company name, my website: www.kev-pro.example , my email: dan@kev-pro.example
Nice to have
• Variations of the colors scheme of a redish-orange (C:0,M:84,Y:100,K:0), grey, white, black. Logo, card, or text can be in any of these colors.
• Possible quote like "Take control of your personal health to unleash your greatest potential" or "Unleashing your greatness first begins with fitness of the body and mind"

```html
<!DOCTYPE html>
<html lang="en">
<head>
<meta charset="utf-8">
<title>KEV.PRO Business Card</title>
<link rel="stylesheet" href="https://fonts.googleapis.com/css2?family=Open+Sans:wght@400;600&display=swap">
<style>
  :root {
    --orange: #f04e23;
    --black: #1a1a1a;
    --card-dark: #2a2a2a;
    --white: #ffffff;
    --grey: #9d9d9d;
    --backdrop: #e6e4e1;
  }
  * { margin: 0; padding: 0; box-sizing: border-box; }
  html, body { width: 1200px; height: 900px; overflow: hidden; }
  body { background: var(--backdrop); position: relative; font-family: "Open Sans", sans-serif; }

  .card {
    position: absolute;
    width: 760px;
    height: 420px;
    border-radius: 4px;
    overflow: hidden;
    box-shadow: 0 10px 28px rgba(0,0,0,0.22);
  }

  /* Back card */
  .card-back { left: 360px; top: 30px; background: var(--card-dark); }
  .card-back .brand { position: absolute; left: 0; right: 0; top: 120px; justify-content: center; }
  .card-back .tagline {
    position: absolute; left: 0; right: 0; top: 255px;
    text-align: center; color: var(--white);
    font-size: 20px; font-weight: 600; letter-spacing: 1.5px; line-height: 1.25;
    text-transform: uppercase;
  }

  .brand { display: flex; align-items: center; gap: 14px; }
  .brand-dot { width: 40px; height: 40px; border-radius: 50%; flex: none; }
  .brand-name { font-family: "Open Sans", sans-serif; font-weight: 400; font-size: 34px; line-height: 1; }
  .card-back .brand-dot { background: var(--white); }
  .card-back .brand-name { color: var(--white); }

  /* Front card */
  .card-front { left: 80px; top: 460px; background: var(--white); }
  .front-shapes { position: absolute; inset: 0; }
  .person { position: absolute; left: 86px; top: 20px; }
  .person-name { color: var(--orange); font-size: 30px; font-weight: 400; line-height: 1.1; }
  .person-role { color: var(--black); font-size: 17px; }

  .contact { position: absolute; left: 36px; top: 180px; list-style: none; }
  .contact li { display: flex; align-items: center; gap: 12px; font-size: 19px; color: var(--black); line-height: 1.45; }
  .contact svg { width: 14px; height: 14px; fill: var(--orange); flex: none; }

  .card-front .brand { position: absolute; left: 430px; top: 175px; }
  .card-front .brand-dot { background: var(--orange); }
  .card-front .brand-name { color: var(--black); }
</style>
</head>
<body>

<section class="card card-back">
  <div class="brand">
    <span class="brand-dot"></span>
    <span class="brand-name">KEV.PRO</span>
  </div>
  <p class="tagline">Take control of your personal health to unleash<br>your greatest potential</p>
</section>

<section class="card card-front">
  <svg class="front-shapes" width="760" height="420" viewBox="0 0 760 420" aria-hidden="true">
    <polygon points="0,0 46,0 20,38 0,38" fill="var(--orange)"/>
    <polygon points="46,0 70,0 70,38 20,38" fill="var(--black)"/>
    <polygon points="0,292 300,292 284,318 0,318" fill="var(--orange)"/>
    <polygon points="300,328 760,328 760,392 260,392" fill="var(--black)"/>
  </svg>

  <div class="person">
    <p class="person-name">Marcus Reed</p>
    <p class="person-role">Managing Director</p>
  </div>

  <ul class="contact">
    <li>
      <svg viewBox="0 0 24 24"><path d="M6.6 10.8a15.1 15.1 0 0 0 6.6 6.6l2.2-2.2a1 1 0 0 1 1-.25 11.4 11.4 0 0 0 3.6.57 1 1 0 0 1 1 1V20a1 1 0 0 1-1 1A17 17 0 0 1 3 4a1 1 0 0 1 1-1h3.5a1 1 0 0 1 1 1c0 1.25.2 2.45.57 3.57a1 1 0 0 1-.25 1z"/></svg>
      044-987 654 321
    </li>
    <li>
      <svg viewBox="0 0 24 24"><path d="M2 5h20v14H2z M2 5l10 8 10-8" stroke="var(--white)" stroke-width="1.5"/></svg>
      dan@kev-pro.example
    </li>
    <li>
      <svg viewBox="0 0 24 24"><path d="M10.6 13.4a1 1 0 0 1 0-1.4l3.5-3.5a1 1 0 1 1 1.4 1.4l-3.5 3.5a1 1 0 0 1-1.4 0zM7 21a4 4 0 0 1-2.8-6.8l3-3 1.4 1.4-3 3A2 2 0 0 0 8.4 18.4l3-3 1.4 1.4-3 3A4 4 0 0 1 7 21zm9.8-8.2-1.4-1.4 3-3A2 2 0 0 0 15.6 5.6l-3 3-1.4-1.4 3-3a4 4 0 0 1 5.6 5.6z"/></svg>
      www.kev-pro.example
    </li>
  </ul>

  <div class="brand">
    <span class="brand-dot"></span>
    <span class="brand-name">KEV.PRO</span>
  </div>
</section>

</body>
</html>
```